Design layout of business card

Create a business card using existing logo and company information.
Our newly established business provides advice to family owned businesses for their succession planning, value improvement and also on business sales and acquisitions.

Target Market(s)

Owners of family businesses

Contact Information for Business Card

Key contact details are:
Greg Holloway
Director
P: 08 9342 5817
W: 0431 587 209
Address: Unit 4, 15 Kestrel Lane, Dunsborough, WA, 6281
Website: kinventureadvisory.com.au
Email: greg@kinventureadvisory.com.au

In smaller font somewhere needs to be these details:
ABN: 47 219 583 906
Licensed Real Estate & Business Agent No. RA53174
QTN Licensee Services Pty Ltd
AFSL No. 527361

Font styles to use
Sans Serif

Requirements
Must have
• Kin Venture Advisory logo to feature on front.
• Remaining logos to be included smaller and on back.
• Orla Business Sales logo to have words 'Powered by' next to it and to be the first of the uploaded logo files.
• Colours on card should complement the logo
Nice to have
• Clear and clean layout
• Logos for contact details for conciseness e.g. phone icon for mobile

```html
<!DOCTYPE html>
<html lang="en">
<head>
<meta charset="utf-8">
<title>Kin Venture Advisory – Business Card</title>
<link rel="stylesheet" href="https://fonts.googleapis.com/css2?family=Poppins:wght@400;500;600;700&display=swap">
<style>
  :root {
    --orange: #f05a28;
    --grey: #9aa3ab;
    --grey-dark: #4a4f55;
    --navy: #1f3f8a;
    --white: #ffffff;
    --backdrop: #d9d8d4;
  }
  * { box-sizing: border-box; margin: 0; padding: 0; }
  html, body { width: 1200px; height: 801px; overflow: hidden; }
  body {
    background: var(--backdrop);
    font-family: "Poppins", sans-serif;
    position: relative;
  }
  .card {
    position: absolute;
    top: 246px;
    width: 540px;
    height: 309px;
    overflow: hidden;
    box-shadow: 0 6px 18px rgba(0,0,0,.18);
  }

  /* ---------- Contact side ---------- */
  .card--contact { left: 40px; background: var(--white); }
  .brand {
    position: absolute; top: 34px; right: 70px;
    display: flex; align-items: center; gap: 14px;
  }
  .brand__ring {
    width: 58px; height: 58px; border-radius: 50%;
    border: 4px solid var(--grey);
  }
  .brand__name {
    color: var(--orange); font-weight: 700;
    font-size: 22px; line-height: 1.05;
  }
  .address {
    position: absolute; top: 128px; right: 40px;
    text-align: right; color: var(--grey-dark);
    font-style: normal;
    font-size: 12px; line-height: 1.45;
  }
  .person {
    position: absolute; left: 56px; top: 120px;
  }
  .person__marker {
    position: absolute; left: -40px; top: 4px;
    width: 26px; height: 26px; background: var(--orange);
  }
  .person__name { color: var(--orange); font-weight: 600; font-size: 22px; line-height: 1.1; }
  .person__role { color: var(--grey-dark); font-weight: 600; font-size: 14px; margin-bottom: 8px; }
  .details { list-style: none; color: var(--grey-dark); font-size: 11px; line-height: 1.55; }
  .details li { display: flex; align-items: center; gap: 6px; white-space: nowrap; }
  .details svg { width: 11px; height: 11px; fill: var(--orange); flex: none; }
  .licence-band {
    position: absolute; left: 0; bottom: 0;
    width: 78%; height: 30px; background: var(--orange);
    color: var(--white); font-size: 12px; font-weight: 500;
    display: flex; align-items: center; padding-left: 56px;
    white-space: nowrap;
  }
  .licence-band__end {
    position: absolute; right: 0; bottom: 0;
    width: 22%; height: 40px; background: var(--grey);
    border-left: 6px solid var(--white);
  }

  /* ---------- Brand side ---------- */
  .card--brand { left: 620px; background: var(--orange); }
  .hero {
    position: absolute; top: 58px; left: 0; right: 0;
    display: flex; justify-content: center; align-items: center; gap: 22px;
  }
  .hero__ring {
    width: 104px; height: 104px; border-radius: 50%;
    border: 6px solid var(--white);
  }
  .hero__name {
    color: var(--white); font-weight: 700;
    font-size: 34px; line-height: 1.02;
  }
  .partners {
    position: absolute; left: 0; right: 0; bottom: 14px;
    height: 62px; background: var(--white);
    display: flex; align-items: center; gap: 16px; padding: 0 22px;
    white-space: nowrap;
  }
  .partners__label { color: var(--grey-dark); font-size: 17px; font-weight: 500; }
  .badge {
    width: 38px; height: 38px; border-radius: 50%; flex: none;
    border: 3px solid var(--navy); background: #e8edf7;
  }
  .partner-text { color: var(--navy); font-weight: 600; font-size: 13px; letter-spacing: 1px; line-height: 1.1; }
  .partner-text small { display: block; font-size: 6px; font-weight: 400; letter-spacing: .3px; color: var(--grey-dark); }
  .partner-orla { display: flex; align-items: center; gap: 6px; color: var(--grey-dark); font-size: 7px; font-weight: 500; letter-spacing: 1px; }
  .partner-orla__square { width: 14px; height: 14px; background: var(--grey-dark); flex: none; }
  .base-stripe {
    position: absolute; left: 0; right: 0; bottom: 0;
    height: 14px; background: var(--grey);
  }
</style>
</head>
<body>

<section class="card card--contact">
  <div class="brand">
    <div class="brand__ring"></div>
    <div class="brand__name">Kin<br>Venture<br>Advisory</div>
  </div>

  <address class="address">
    QTN Licensee Services Pty Ltd<br>
    Unit 4, 15 Kestrel Lane,<br>
    Marlow Bay, SA, 5291
  </address>

  <div class="person">
    <span class="person__marker"></span>
    <h1 class="person__name">Greg Holloway</h1>
    <p class="person__role">Director</p>
    <ul class="details">
      <li>ABN: 47 219 583 906</li>
      <li>AFSL No. 527361</li>
      <li><svg viewBox="0 0 24 24"><path d="M6.6 10.8a15.1 15.1 0 0 0 6.6 6.6l2.2-2.2a1 1 0 0 1 1-.25 11.4 11.4 0 0 0 3.6.57 1 1 0 0 1 1 1V20a1 1 0 0 1-1 1A17 17 0 0 1 3 4a1 1 0 0 1 1-1h3.5a1 1 0 0 1 1 1c0 1.25.2 2.450.57 3.57a1 1 0 0 1-.25 1z"/></svg>08 9342 5817</li>
      <li><svg viewBox="0 0 24 24"><rect x="6" y="2" width="12" height="20" rx="2"/><rect x="8" y="4" width="8" height="13" fill="#fff"/></svg>0431 587 209</li>
      <li><svg viewBox="0 0 24 24"><path d="M2 5h20v14H2z"/><path d="M2 5l10 8 10-8" fill="none" stroke="#fff" stroke-width="2"/></svg>greg@kinventureadvisory.com.au</li>
      <li><svg viewBox="0 0 24 24"><circle cx="12" cy="12" r="10"/><path d="M2 12h20M12 2c3 3 3 17 0 20M12 2c-3 3-3 17 0 20" fill="none" stroke="#fff" stroke-width="1.5"/></svg>www.kinventureadvisory.com.au</li>
    </ul>
  </div>

  <div class="licence-band">Licensed Real Estate &amp; Business Agent No. RA53174</div>
  <div class="licence-band__end"></div>
</section>

<section class="card card--brand">
  <div class="hero">
    <div class="hero__ring"></div>
    <div class="hero__name">Kin<br>Venture<br>Advisory</div>
  </div>

  <div class="partners">
    <span class="partners__label">Powered by</span>
    <span class="badge" role="img" aria-label="Accredited adviser badge"></span>
    <span class="partner-text">Brokers Guild<small>guild of business brokers</small></span>
    <span class="badge" role="img" aria-label="Advisor member badge"></span>
    <span class="partner-orla"><span class="partner-orla__square"></span>THEORLAGROUP.COM.AU</span>
  </div>
  <div class="base-stripe"></div>
</section>

</body>
</html>
```